Medical Implant company needs a Top Quality Premium Brochure

We need to create a top quality brochure for VIP clients, formed by top spine surgeons. The main goal here is to cause a deep quality impact, positioning the company and it´s solutions above the others, with a refined, unique and creative material.

Special paper, hot stamping, innovative format are welcome.

For more information check out our website: www.veltrosan.com.br (web translator are recommended for content understanding)

Veltrosan works with top quality spine and pain management products, providing solutions for the medical specialists, investing in high quality processes and continued medical education.

Short briefing:
1 - Company profile
2 - Quality / vision
3 - Continued education programs
4 - Main products
5 - Main partners
6 - Final stuff (creative final thoughts / considerations)

FORMAT: 25 x 18,5 cm (horizontal)
PAGES - 16

REFERENCES:

https://www.folivenk.net/gallery/52917340/Medical-Healthcare-Profile-Brochure

https://www.folivenk.net/gallery/7810263/TK-Alpine-Style-Brochure

Target Market(s)

Mainly brazilian spine and neuro surgeons with minimally invasive surgery skills.

Industry/Entity Type

Education

Requirements
Must have

• 18 pages design

1. Cover
2. IMAGE + TITLE - About Us
3. IMAGE + TEXT - About Us
4. IMAGE + TITLE - Vision
5. IMAGE + TEXT - Vision
6. IMAGE + TITLE - Quality
7. IMAGE + TEXT - Quality
8. Timeline Left
9. Timeline Right
10. IMAGE + TITLE - Medical Education
11. IMAGE + TEXT - Medical Education
12. IMAGE + TITLE - Minimally Invasive Technology
13. IMAGE + TEXT - Minimally Invasive Technology
14. IMAGE + TITLE - Impact Phrase
15. IMAGE + TEXT - Impact Phrase
16. Back

As longs as the text is under development and will be placed internally in the winning design, please use 'lorem ipsum' for text areas. The titles can follow the index above.

Nice to have
• The use of office pictures with some style / artistic finish in pages "about us"

```html
<!DOCTYPE html>
<html lang="en">
<head>
<meta charset="utf-8">
<title>Veltrosan Brochure – Chapter One Spread</title>
<link rel="stylesheet" href="https://fonts.googleapis.com/css2?family=Open+Sans:ital,wght@0,400;0,600;0,700;1,400;1,600&display=swap">
<style>
  :root {
    --bg: #e4e4e4;
    --paper: #ffffff;
    --green: #1f9a5a;
    --green-soft: #3aa96f;
    --text: #3c3c3c;
    --muted: #7a7a7a;
    --gold: #d7a928;
    --panel: #ecebe3;
    --grid: #ffffff;
  }
  * { box-sizing: border-box; margin: 0; padding: 0; }
  html, body { width: 1200px; height: 900px; overflow: hidden; }
  body { background: var(--bg); font-family: "Open Sans", Arial, sans-serif; color: var(--text); }

  .spread {
    position: absolute; left: 40px; top: 243px;
    width: 1120px; height: 414px; display: flex;
    box-shadow: 0 10px 30px rgba(0,0,0,.18);
  }
  .page { position: relative; width: 560px; height: 414px; background: var(--paper); overflow: hidden; }
  .page--left { border-right: 1px solid #ddd; }

  .photo { position: absolute; }
  .chapter-tab {
    position: absolute; background: var(--green); color: #fff;
    font-size: 6.5px; font-weight: 600; letter-spacing: .8px; text-transform: uppercase;
    display: flex; align-items: center; justify-content: center; height: 18px;
  }
  .folio {
    position: absolute; bottom: 14px; width: 16px; height: 16px; background: var(--green);
    color: #fff; font-size: 7px; font-weight: 700; display: flex; align-items: center; justify-content: center;
  }

  /* left page */
  .photo--hero { left: 110px; top: 0; width: 220px; height: 100px; background: linear-gradient(120deg, #0f6f7a, #6fc3c8 60%, #d9eef0); }
  .photo--doctor { left: 28px; top: 104px; width: 84px; height: 58px; background: linear-gradient(135deg, #f3ece8, #c9b7ae); }
  .photo--pills { left: 118px; top: 104px; width: 88px; height: 58px; background: linear-gradient(135deg, #c43a32, #e8d9cf 55%, #f5f2ec); }
  .page--left .chapter-tab { left: 240px; top: 12px; width: 92px; }
  .caption { position: absolute; top: 170px; width: 82px; font-size: 5.5px; line-height: 1.45; color: var(--muted); }
  .caption h4 { color: var(--gold); font-size: 6px; font-weight: 700; margin-bottom: 2px; }
  .caption--a { left: 28px; }
  .caption--b { left: 118px; }

  .chart-panel { position: absolute; left: 216px; top: 100px; width: 332px; height: 300px; background: var(--panel); }
  .chart-panel svg { display: block; }
  .chart-title { font-size: 6px; fill: var(--muted); }
  .axis-label { font-size: 6px; fill: #666; font-family: "Open Sans", Arial, sans-serif; }

  /* right page */
  .quote { position: absolute; left: 170px; top: 24px; width: 370px; color: var(--green); font-style: italic; }
  .quote__lead { font-size: 13.5px; line-height: 1.3; }
  .quote__rest { font-size: 9.5px; line-height: 1.35; }
  .page--right .chapter-tab { right: 0; top: 110px; width: 88px; }
  .feature { position: absolute; width: 150px; }
  .feature .photo { position: static; width: 150px; height: 72px; }
  .feature h3 { color: var(--green); font-size: 8px; font-weight: 700; line-height: 1.2; margin: 6px 0 4px; }
  .feature p { font-size: 6.5px; line-height: 1.5; color: var(--text); }
  .feature--one { left: 25px; top: 82px; }
  .feature--two { left: 195px; top: 122px; }
  .feature--three { left: 365px; top: 160px; }
  .photo--team { background: linear-gradient(135deg, #e9f0f4, #bcd0dc); }
  .photo--lab { background: linear-gradient(135deg, #9fd0e6, #e8f3f8); }
  .photo--staff { background: linear-gradient(135deg, #f4f6f8, #a9c4d8); }
  .page--left .folio { left: 28px; }
  .page--right .folio { right: 28px; }
</style>
</head>
<body>
<main class="spread">
  <section class="page page--left">
    <div class="photo photo--hero" role="img" aria-label="Close-up of a surgeon in cap and mask"></div>
    <div class="chapter-tab">Chapter One</div>
    <div class="photo photo--doctor" role="img" aria-label="Doctor in a surgical mask"></div>
    <div class="photo photo--pills" role="img" aria-label="Assorted medicine capsules"></div>
    <div class="caption caption--a">
      <h4>Health Care</h4>
      <p>Lorem ipsum dolor sit amet, consectetur adipiscing elit. Nulla vitae elit libero, a pharetra augue sed posuere.</p>
    </div>
    <div class="caption caption--b">
      <h4>Lab Supplies</h4>
      <p>Donec sed odio dui, etiam porta sem malesuada magna mollis euismod. Cras justo odio dapibus ac facilisis.</p>
    </div>

    <div class="chart-panel">
      <svg width="332" height="300" viewBox="0 0 332 300">
        <text class="chart-title axis-label" x="60" y="22">Annual revenue growth</text>
        <g stroke="var(--grid)" stroke-width="1">
          <line x1="50" y1="30" x2="312" y2="30"/>
          <line x1="50" y1="90" x2="312" y2="90"/>
          <line x1="50" y1="150" x2="312" y2="150"/>
          <line x1="50" y1="210" x2="312" y2="210"/>
          <line x1="50" y1="270" x2="312" y2="270"/>
          <line x1="50" y1="30" x2="50" y2="270"/>
          <line x1="93.7" y1="30" x2="93.7" y2="270"/>
          <line x1="137.3" y1="30" x2="137.3" y2="270"/>
          <line x1="181" y1="30" x2="181" y2="270"/>
          <line x1="224.7" y1="30" x2="224.7" y2="270"/>
          <line x1="268.3" y1="30" x2="268.3" y2="270"/>
          <line x1="312" y1="30" x2="312" y2="270"/>
        </g>
        <polygon points="50,150 93.7,95 118,55 150,90 190,120 230,200 268.3,240 312,185 312,270 50,270" fill="#a3a3a3"/>
        <polygon points="50,170 93.7,150 137.3,175 181,190 224.7,205 268.3,245 312,270 50,270" fill="var(--green-soft)" opacity=".9"/>
        <polygon points="224.7,205 268.3,245 312,270 312,185 268.3,240 230,200" fill="#5f5f5f" opacity=".7"/>
        <g class="axis-label" text-anchor="end">
          <text x="44" y="32">6,000</text>
          <text x="44" y="92">4,800</text>
          <text x="44" y="152">3,600</text>
          <text x="44" y="212">2,400</text>
          <text x="44" y="272">1,200</text>
        </g>
        <g class="axis-label" text-anchor="middle">
          <text x="50" y="285">2006</text>
          <text x="93.7" y="285">2008</text>
          <text x="137.3" y="285">2010</text>
          <text x="181" y="285">2012</text>
          <text x="224.7" y="285">2014</text>
          <text x="268.3" y="285">2016</text>
          <text x="312" y="285">2018</text>
        </g>
      </svg>
    </div>
    <div class="folio">8</div>
  </section>

  <section class="page page--right">
    <div class="quote">
      <p class="quote__lead">Planning is an unnatural process; it is much more fun to do something.</p>
      <p class="quote__rest">The nicest thing about not planning is that failure comes as a complete surprise, rather than being preceded by a period of worry and depression.</p>
    </div>
    <div class="chapter-tab">Chapter One</div>

    <article class="feature feature--one">
      <div class="photo photo--team" role="img" aria-label="Group of smiling medical staff"></div>
      <h3>More business is lost every year through neglect than other</h3>
      <p>Donec sed odio dui. Nulla vitae elit libero, a pharetra augue. Nulla vitae elit id elit. Integer posuere erat a ante venenatis dapibus posuere velit aliquet. Etiam porta sem nec elit quam.</p>
    </article>

    <article class="feature feature--two">
      <div class="photo photo--lab" role="img" aria-label="Doctor reviewing an x-ray scan"></div>
      <h3>The people who make art their business are mostly imposters</h3>
      <p>Sunt explicabo. Nemo enim ipsam voluptatem quia voluptas sit aspernatur aut odit aut fugit, sed quia consequuntur magni dolores eos qui ratione voluptatem sequi nesciunt. Expedita distinctio nam libero tempore odio sem nec elit.</p>
    </article>

    <article class="feature feature--three">
      <div class="photo photo--staff" role="img" aria-label="Team of doctors and nurses standing together"></div>
      <h3>No price is too low for a bear or too high for a bull</h3>
      <p>Donec sed odio dui duis mollis, est non com luctus, nisi erat porttitor ligula, eget lacinia odio sem nec elit. Sed posuere consectetur est at lobortis. Nulla vitae elit libero, a pharetra augue. Donec ullamcorper nulla non metus auctor fringilla.</p>
    </article>
    <div class="folio">9</div>
  </section>
</main>
</body>
</html>
```